Poster for Ballet Recital Tomasito y el Espejo Encantado

We need a poster for a ballet performance, we will be presenting "Tomasito y el Espejo Encantado".
We need something that looks magical, the word Tomasito as the main title in 3D gold texture and the text y el Espejo Encantado way smaller. We have included a reference of the Brelvo movie, just because we like the starry night background and the glowing moon. We don't want the two characters nor the flying carpet, because we will be adding a photo later.
The idea is for the poster to look magical, mysterious but fun. We want people to get the idea that the show will be very entertaining and worth their money.

Font styles to use
Decorative
Script

Colors

Designer to choose colors to be used in the design.

Requirements
Must have
• The title: Tomasito y el Espejo Encantado
• It must also include space for adding the ballet company logo, the dates, times and prices.
Nice to have
• Magical feel
Should not have
• Any photo or character illustration

```html
<!DOCTYPE html>
<html lang="es">
<head>
<meta charset="utf-8">
<title>Tomasito y el Espejo Encantado</title>
<link rel="stylesheet" href="https://fonts.googleapis.com/css2?family=Great+Vibes&display=swap">
<style>
  :root {
    --navy-deep: #0c2644;
    --navy: #12345a;
    --teal: #2b6f8f;
    --teal-light: #5fa6c2;
    --glow: #e8f6ff;
    --gold-pale: #fff1b8;
    --gold-light: #f7d774;
    --gold: #d9a42c;
    --gold-dark: #8a5a12;
    --subtitle: #ffffff;
  }
  * { margin: 0; padding: 0; box-sizing: border-box; }
  html, body {
    width: 848px;
    height: 1200px;
    overflow: hidden;
    background: var(--navy-deep);
  }
  .poster {
    position: relative;
    width: 848px;
    height: 1200px;
    overflow: hidden;
    background:
      radial-gradient(ellipse 260px 300px at 470px 340px, rgba(232,246,255,0.95) 0%, rgba(150,210,235,0.55) 35%, rgba(60,140,180,0) 75%),
      radial-gradient(ellipse 520px 380px at 480px 380px, rgba(95,166,194,0.55) 0%, rgba(43,111,143,0) 80%),
      radial-gradient(ellipse 300px 200px at 90px 200px, rgba(120,170,195,0.35) 0%, rgba(120,170,195,0) 80%),
      radial-gradient(ellipse 260px 180px at 60px 500px, rgba(120,170,195,0.3) 0%, rgba(120,170,195,0) 80%),
      linear-gradient(180deg, var(--teal) 0%, #1f5879 35%, var(--navy) 62%, var(--navy-deep) 100%);
  }
  .sky-stars {
    position: absolute;
    inset: 0;
    width: 848px;
    height: 1200px;
  }
  .hero-art {
    position: absolute;
    left: 110px;
    top: 224px;
    width: 560px;
    height: 500px;
    background:
      radial-gradient(closest-side, rgba(255,241,184,0.95) 0%, rgba(247,215,116,0.9) 30%, rgba(217,164,44,0.75) 55%, rgba(138,90,18,0.3) 80%, rgba(138,90,18,0) 100%);
  }
  .title-block {
    position: absolute;
    left: 0;
    top: 728px;
    width: 848px;
    text-align: center;
    font-family: "Great Vibes", cursive;
    font-weight: 400;
  }
  .title-main {
    display: inline-block;
    font-size: 156px;
    line-height: 1.05;
    padding: 0 30px;
    background: linear-gradient(180deg, var(--gold-pale) 0%, var(--gold-light) 35%, var(--gold) 60%, var(--gold-dark) 100%);
    -webkit-background-clip: text;
    background-clip: text;
    color: transparent;
    filter: drop-shadow(0 3px 0 #6b4409) drop-shadow(0 6px 8px rgba(0,0,0,0.45));
  }
  .title-sub {
    display: block;
    margin-top: -8px;
    font-size: 60px;
    line-height: 1.1;
    color: var(--subtitle);
  }
</style>
</head>
<body>
  <main class="poster">
    <svg class="sky-stars" viewBox="0 0 848 1200" aria-hidden="true">
      <g fill="#ffffff">
        <circle cx="420" cy="40" r="2"/>
        <circle cx="380" cy="90" r="2.5"/>
        <circle cx="450" cy="120" r="1.8"/>
        <circle cx="400" cy="170" r="2.2"/>
        <circle cx="500" cy="150" r="1.6"/>
        <circle cx="350" cy="220" r="2"/>
        <circle cx="470" cy="210" r="2.4"/>
        <circle cx="290" cy="180" r="1.5"/>
        <circle cx="540" cy="250" r="1.8"/>
        <circle cx="660" cy="100" r="5" opacity="0.8"/>
        <circle cx="170" cy="60" r="3" opacity="0.7"/>
        <circle cx="150" cy="390" r="2" opacity="0.8"/>
        <circle cx="630" cy="410" r="2" opacity="0.8"/>
      </g>
    </svg>
    <div class="hero-art" role="img" aria-label="Espejo encantado dorado y ornamentado, con un rastro de destellos mágicos que sube hacia el cielo"></div>
    <h1 class="title-block">
      <span class="title-main">Tomasito</span>
      <span class="title-sub">y el Espejo Encantado</span>
    </h1>
  </main>
</body>
</html>
```